Now Hiring Drivers or Help Wanted Ad

I am looking for an ad to be used for digital marketing for employment. Below is some or all of the information to work into the ad.

Tavrin Haulage, LLC is a stable and premier hauler operating in the Northeast Wisconsin region since 1994. We have a variety of equipment from Dump Trucks, Roll Off Trucks to Semis with Belt Trailers, Walking Floors, Gondolas, Tankers, Vans and Compacting Trailers offering a variety of positions with different routes to mix up your day or settle into something you enjoy. We also offer low boy services and some flat bed work. We haul various materials from general aggregate freight to various types of non-hazardous wastes such as garbage, recyclables, paper mill sludge, metal, shredder fluff to various landfills or recycling centers.

Rate of pay is based on experience and the variety of equipment you are able to operate or your willingness to learn.

All work is local and you are home every night.

Great Pay
Sign on Bonus
Holiday & Vacation Pay
Health Insurance, Vision & Dental Offered
Employer Paid Life Insurance
Uniforms
Phone Reimbursement
VORIX

Industry/Entity Type

Trucking and Excavation

Colors
EB3D1F
EC4F4E
F09395
F8D3D4
FCEDEE

Requirements
Must have
• Should have some of the same look/feel of the ad attached.

```html
<!DOCTYPE html>
<html lang="en">
<head>
<meta charset="utf-8">
<title>Now Hiring Drivers – Tavrin Haulage, LLC</title>
<link rel="stylesheet" href="https://fonts.googleapis.com/css2?family=Bebas+Neue&family=Montserrat:wght@400;600;700&display=swap">
<style>
  :root{
    --green:#56b45a;
    --yellow:#f4c51c;
    --red:#e8232a;
    --white:#ffffff;
    --ink:#2a2a2a;
    --backdrop:#f2f2f2;
    --photo-truck-a:#6c8f4e;
    --photo-truck-b:#b3262c;
    --photo-person-a:#e9ecef;
    --photo-person-b:#33447a;
  }
  html,body{margin:0;padding:0;width:1200px;height:2182px;overflow:hidden;background:var(--backdrop);}
  .flyer{
    position:absolute;left:0;top:314px;width:754px;height:976px;
    transform:scale(1.5915);transform-origin:0 0;
    background:var(--white);overflow:hidden;
    font-family:"Montserrat",sans-serif;color:var(--ink);
  }
  .layer{position:absolute;inset:0;}
  .headline{position:absolute;left:48px;top:22px;margin:0;font-family:"Bebas Neue",sans-serif;font-weight:400;line-height:0.86;font-size:92px;letter-spacing:-0.5px;}
  .headline .now{color:var(--white);display:block;}
  .headline .role{color:var(--red);display:block;}
  .brand{position:absolute;left:470px;top:92px;width:270px;display:flex;align-items:center;gap:10px;justify-content:center;}
  .brand-name{font-family:"Montserrat",sans-serif;font-weight:700;color:var(--green);font-size:24px;line-height:1.05;text-align:center;}
  .brand-dot{width:16px;height:16px;border-radius:50%;background:var(--red);flex:none;}
  .tagline{position:absolute;left:50px;top:206px;margin:0;font-weight:700;font-size:24px;line-height:1.18;color:var(--ink);}
  .about{position:absolute;right:40px;top:212px;width:260px;margin:0;text-align:right;font-size:14.4px;line-height:17.7px;color:var(--ink);}
  .pay-note{position:absolute;left:0;top:670px;width:754px;margin:0;text-align:center;color:var(--white);font-weight:700;font-size:17px;line-height:21px;}
  .benefits{position:absolute;left:40px;top:742px;width:420px;display:grid;grid-template-columns:180px 240px;grid-auto-rows:56px;margin:0;padding:0;list-style:none;}
  .benefit{display:flex;align-items:center;gap:10px;font-weight:700;font-size:12.5px;line-height:1.25;}
  .benefit-icon{width:48px;height:48px;border-radius:50%;background:var(--yellow);flex:none;display:flex;align-items:center;justify-content:center;}
  .benefit-icon svg{width:26px;height:26px;fill:none;stroke:var(--ink);stroke-width:1.8;stroke-linecap:round;stroke-linejoin:round;}
  .call{position:absolute;right:34px;top:922px;margin:0;font-weight:700;font-size:31px;color:var(--white);letter-spacing:0.5px;}
  .call .label{color:var(--yellow);}
</style>
</head>
<body>
<main class="flyer">
  <svg class="layer" viewBox="0 0 754 976" aria-hidden="true">
    <defs>
      <linearGradient id="truckPhoto" x1="0" y1="0" x2="1" y2="1">
        <stop offset="0" stop-color="var(--photo-truck-a)"/>
        <stop offset="0.55" stop-color="var(--photo-truck-b)"/>
        <stop offset="1" stop-color="#3f6d32"/>
      </linearGradient>
      <linearGradient id="personPhoto" x1="0" y1="0" x2="1" y2="0">
        <stop offset="0" stop-color="var(--white)"/>
        <stop offset="0.45" stop-color="var(--photo-person-a)"/>
        <stop offset="1" stop-color="var(--photo-person-b)"/>
      </linearGradient>
    </defs>
    <rect class="about-panel" x="0" y="196" width="754" height="476" fill="var(--yellow)"/>
    <polygon class="header-green" points="0,0 396,0 430,196 0,196" fill="var(--green)"/>
    <polygon class="header-rule" points="396,0 406,0 440,196 430,196" fill="var(--red)"/>
    <polygon class="header-sheen" points="430,196 470,196 470,272 430,272" fill="var(--yellow)"/>
  </svg>

  <svg class="layer" viewBox="0 0 754 976">
    <polygon points="0,272 458,272 518,672 0,672" fill="url(#truckPhoto)" role="img" aria-label="Photo of a driver in a hi-vis shirt standing beside a red dump truck"/>
    <polygon points="450,735 754,735 754,922 450,922" fill="url(#personPhoto)" role="img" aria-label="Photo of a smiling driver in a blue cap and work jacket beside a white truck"/>
  </svg>

  <svg class="layer" viewBox="0 0 754 976" aria-hidden="true">
    <rect class="pay-band" x="0" y="668" width="754" height="62" fill="var(--red)"/>
    <polygon class="call-band" points="404,920 754,920 754,976 384,976" fill="var(--red)"/>
    <rect class="base-rule" x="0" y="968" width="754" height="8" fill="var(--red)"/>
  </svg>

  <h1 class="headline"><span class="now">Now Hiring</span><span class="role">Drivers</span></h1>

  <div class="brand">
    <span class="brand-name">TAVRIN<br>HAULAGE, LLC</span>
    <span class="brand-dot"></span>
  </div>

  <p class="tagline">All work is local and you<br>are home every night.</p>

  <p class="about">Tavrin Haulage, LLC is a stable<br>and premier hauler operating in<br>the Northeast Wisconsin region<br>since 1994. We have a variety of<br>equipment from Dump Trucks,<br>Roll Off Trucks to Semis with<br>Belt Trailers, Walking Floors,<br>Gondolas, Tankers, Vans and<br>Compacting Trailers offering a<br>variety of positions with<br>different routes to mix up your<br>day or settle into something<br>you enjoy. We also offer low<br>boy services and some flat<br>bed work. We haul various<br>materials from general<br>aggregate freight to<br>various types of<br>non-hazardous wastes<br>such as garbage,<br>recyclables, paper<br>mill sludge, metal,<br>shredder fluff to<br>various landfills<br>or recycling centers.</p>

  <p class="pay-note">Rate of pay is based on experience and the variety of equipment<br>you are able to operate or your willingness to learn.</p>

  <ul class="benefits">
    <li class="benefit"><span class="benefit-icon"><svg viewBox="0 0 24 24"><rect x="4" y="6" width="16" height="12" rx="1"/><circle cx="12" cy="12" r="3"/></svg></span>Great Pay</li>
    <li class="benefit"><span class="benefit-icon"><svg viewBox="0 0 24 24"><path d="M12 20s-7-4.5-7-9.5A3.5 3.5 0 0 1 12 8a3.5 3.5 0 0 1 7 2.5C19 15.5 12 20 12 20z"/></svg></span>Health Insurance,<br>Vision &amp; Dental Offered</li>
    <li class="benefit"><span class="benefit-icon"><svg viewBox="0 0 24 24"><rect x="4" y="10" width="16" height="10"/><path d="M3 7h18v3H3zM12 7v13"/></svg></span>Sign on Bonus</li>
    <li class="benefit"><span class="benefit-icon"><svg viewBox="0 0 24 24"><path d="M12 3l7 3v5c0 5-3.5 8-7 10-3.5-2-7-5-7-10V6z"/></svg></span>Employer Paid<br>Life Insurance</li>
    <li class="benefit"><span class="benefit-icon"><svg viewBox="0 0 24 24"><rect x="4" y="5" width="16" height="15" rx="1"/><path d="M4 10h16M8 3v4M16 3v4"/></svg></span>Holiday &amp;<br>Vacation Pay</li>
    <li class="benefit"><span class="benefit-icon"><svg viewBox="0 0 24 24"><path d="M6 3h3l2 5-2 1.5a11 11 0 0 0 5.5 5.5L16 13l5 2v3a2 2 0 0 1-2 2A16 16 0 0 1 4 5a2 2 0 0 1 2-2z"/></svg></span>Phone<br>Reimbursement</li>
    <li class="benefit"><span class="benefit-icon"><svg viewBox="0 0 24 24"><rect x="5" y="8" width="14" height="11" rx="1"/><path d="M9 8V5h6v3"/></svg></span>VORIX</li>
    <li class="benefit"><span class="benefit-icon"><svg viewBox="0 0 24 24"><path d="M8 3l4 3 4-3 4 4-3 3v10H7V10L4 7z"/></svg></span>Uniforms</li>
  </ul>

  <p class="call"><span class="label">Call</span>-0123456789</p>
</main>
</body>
</html>
```